Funky Business card design for starting out career counsellor - Melbourne, Australia

Hi there, I am seeking a business card design to send straight to print. I work from a psycho-spiritual framework (existential, non-dual, transpersonal) framework and was hoping for something that is modern, funky - yet has an established grounded feel to it, but pushes the edge of art and boundary. Minimal design is good.
I don't have a corporate identity other than my wordpress template at www.pathwaylanternhub.com. I like the depth of the this wordpress template, with the thought provaking image. A design that aligns to the wordpress template would be awesome (but unique is okay too).
Thanks for your help :)
Contact details for card:
Marcus Belvane Registered Career Counsellor marcus@pathwaylanternhub.com
(existential, non-dual, transpersonal)
www.pathwaylanternhub.com +61 (0) 482 916 204 Melbourne CBD & Globally on Callwave

```html
<!DOCTYPE html>
<html lang="en">
<head>
<meta charset="utf-8">
<title>Marcus Belvane — Business Card</title>
<link href="https://fonts.googleapis.com/css2?family=Didact+Gothic&family=Dancing+Script:wght@500&display=swap" rel="stylesheet">
<style>
  :root {
    --stage: #4a4a4c;
    --card-dark: #050505;
    --card-light: #ffffff;
    --ink: #111111;
    --ink-soft: #8a8a8a;
    --script-light: #d9d9d9;
    --art-a: #3f6fd6;
    --art-b: #9a4fc8;
    --silver-hi: #f4f4f4;
    --silver-mid: #a8a8a8;
    --silver-lo: #5e5e5e;
  }
  * { margin: 0; padding: 0; box-sizing: border-box; }
  html, body { width: 1200px; height: 922px; overflow: hidden; }
  body {
    background: var(--stage);
    position: relative;
    font-family: "Didact Gothic", sans-serif;
  }
  .card {
    position: absolute;
    width: 640px;
    height: 366px;
    box-shadow: 0 10px 24px rgba(0,0,0,0.45);
    overflow: hidden;
  }
  .card svg { position: absolute; inset: 0; }

  /* Back */
  .card-back { left: 50px; top: 70px; background: var(--card-dark); }
  .tagline {
    position: absolute;
    left: 110px;
    top: 280px;
    font-family: "Dancing Script", cursive;
    font-size: 25px;
    color: var(--script-light);
    letter-spacing: 1px;
    white-space: nowrap;
  }

  /* Front */
  .card-front { left: 510px; top: 486px; background: var(--card-light); }
  .contact {
    position: absolute;
    right: 28px;
    top: 44px;
    text-align: right;
    line-height: 1.1;
    white-space: nowrap;
  }
  .name { font-size: 36px; color: var(--ink); font-weight: 400; letter-spacing: 0.5px; }
  .role { font-size: 15px; color: var(--ink-soft); margin-top: 8px; }
  .role-detail { font-size: 15px; color: var(--ink-soft); margin-top: 2px; }
  .email, .web { font-size: 21px; color: var(--ink); }
  .email { margin-top: 14px; }
  .web { margin-top: 6px; }
  .phone { font-size: 20px; color: var(--ink-soft); margin-top: 22px; }
  .location { font-size: 20px; color: var(--ink-soft); margin-top: 4px; }
  .arc-text {
    font-family: "Dancing Script", cursive;
    font-size: 15px;
    fill: var(--ink);
  }
</style>
</head>
<body>

<section class="card card-back" aria-label="Card back">
  <svg width="640" height="366" viewBox="0 0 640 366">
    <defs>
      <linearGradient id="art-tone" x1="0" y1="0" x2="1" y2="1">
        <stop offset="0%" stop-color="var(--art-a)"/>
        <stop offset="100%" stop-color="var(--art-b)"/>
      </linearGradient>
      <linearGradient id="silver" x1="0" y1="0" x2="1" y2="0">
        <stop offset="0%" stop-color="var(--silver-lo)"/>
        <stop offset="50%" stop-color="var(--silver-hi)"/>
        <stop offset="100%" stop-color="var(--silver-lo)"/>
      </linearGradient>
    </defs>
    <path class="lens" role="img" aria-label="Colourful psychedelic spiral artwork"
          d="M20,150 Q320,-20 620,150 Q320,320 20,150 Z" fill="url(#art-tone)"/>
    <path class="lens-rim" d="M20,150 Q320,-20 620,150" fill="none" stroke="url(#silver)" stroke-width="9"/>
    <path class="lens-rim" d="M20,150 Q320,320 620,150" fill="none" stroke="url(#silver)" stroke-width="9"/>
  </svg>
  <p class="tagline">Discover your authentic self...</p>
</section>

<section class="card card-front" aria-label="Card front">
  <svg width="640" height="366" viewBox="0 0 640 366">
    <defs>
      <linearGradient id="corner-tone" x1="0" y1="0" x2="1" y2="1">
        <stop offset="0%" stop-color="var(--art-a)"/>
        <stop offset="100%" stop-color="var(--art-b)"/>
      </linearGradient>
      <linearGradient id="silver-arc" x1="0" y1="1" x2="1" y2="0">
        <stop offset="0%" stop-color="var(--silver-lo)"/>
        <stop offset="50%" stop-color="var(--silver-hi)"/>
        <stop offset="100%" stop-color="var(--silver-mid)"/>
      </linearGradient>
      <path id="arc-line" d="M0,248 A248,248 0 0 0 248,0"/>
    </defs>
    <path class="corner-art" role="img" aria-label="Corner of colourful psychedelic spiral artwork"
          d="M0,0 L222,0 A222,222 0 0 1 0,222 Z" fill="url(#corner-tone)"/>
    <path class="corner-rim" d="M222,0 A222,222 0 0 1 0,222" fill="none" stroke="url(#silver-arc)" stroke-width="8"/>
    <text class="arc-text"><textPath href="#arc-line" startOffset="4%">...sharing the journey of spiritual awakening</textPath></text>
  </svg>
  <div class="contact">
    <h1 class="name">Marcus Belvane</h1>
    <p class="role">Registered Career Counsellor</p>
    <p class="role-detail">(existential, non-dual, transpersonal)</p>
    <p class="email">marcus@pathwaylanternhub.com</p>
    <p class="web">www.pathwaylanternhub.com</p>
    <p class="phone">+61 (0) 482 916 204</p>
    <p class="location">Melbourne CBD &amp; Globally on Callwave</p>
  </div>
</section>

</body>
</html>
```